Modern business card and stationary design for Tech consulting company (startup)
Veromb Technologies Limited
Modern business card and stationary design for Tech consulting company (startup) - Information Technology
Creative Brief
Professional
Malcolm Dewhurst
CEO
Suite 24613 Lower Ground Floor 212-224 Harwell Road London, N7 2QD
mdewhurst@veromb.co.uk
www.veromb.co.uk
Designers, This project is for business card and stationary design. What I’m looking for is design based around the colour scheme of the attached logo. As yet the website is still being designed, but the attached business logo will give you a reference point for the corporate colours. I have attached a couple of links with a general idea of what I’m looking for; http://www.plandoria.com/drafts/display/contest/518230/draft/3047612 http://www.plandoria.com/drafts/display/contest/518230/draft/3048945 All submitted designs will be rated on a regular basis. If you have any further questions relating to this project, please let get in touch. The winning design will be required to provide editable versions of the files (i.e. personal contact details etc.) Good luck

```html
<!DOCTYPE html>
<html lang="en">
<head>
<meta charset="utf-8">
<title>Veromb Technologies – Stationery</title>
<link rel="stylesheet" href="https://fonts.googleapis.com/css2?family=Open+Sans:ital,wght@0,400;0,600;0,700;1,400&display=swap">
<style>
  :root{
    --red:#c4161c;
    --red-deep:#7d0a0f;
    --red-light:#e2353a;
    --ink:#3d3d3d;
    --ink-soft:#7a7a7a;
    --paper:#ffffff;
    --stage:#e9e6e6;
    --rule:#d9d9d9;
  }
  *{box-sizing:border-box;margin:0;padding:0}
  html,body{width:1200px;height:862px;overflow:hidden}
  body{background:var(--stage);font-family:"Open Sans",Arial,sans-serif;color:var(--ink);position:relative}
  .sheet{position:absolute;background:var(--paper);box-shadow:0 4px 14px rgba(0,0,0,.18);overflow:hidden}
  .brand{display:flex;align-items:center;gap:7px;font-weight:700;color:var(--ink);letter-spacing:.3px;white-space:nowrap}
  .brand__mark{background:var(--red);display:inline-block;flex:none}
  .band{position:absolute;left:0;right:0;bottom:0;background:linear-gradient(90deg,var(--red-deep),var(--red) 55%,var(--red-light));color:#fff;font-style:italic;display:flex;align-items:center;white-space:nowrap}
  .contact{font-size:7px;line-height:1.45;color:var(--ink-soft)}
  .contact strong{color:var(--ink);font-weight:600}
  .body-copy{font-size:8px;line-height:1.6;color:var(--ink-soft)}

  /* letterhead */
  .letterhead{left:40px;top:36px;width:340px;height:480px}
  .letterhead .brand{position:absolute;left:28px;top:30px;font-size:13px}
  .letterhead .brand__mark{width:13px;height:13px}
  .letterhead .contact{position:absolute;right:26px;top:24px;text-align:right}
  .letterhead .greeting{position:absolute;left:28px;top:96px;font-size:13px;color:var(--ink)}
  .letterhead .body-copy{position:absolute;left:28px;right:28px;top:124px}
  .letterhead .band{height:26px;padding-left:28px;font-size:8px}

  /* fax */
  .fax{left:400px;top:36px;width:340px;height:480px}
  .fax__title{position:absolute;right:26px;top:30px;font-size:18px;color:var(--red);font-weight:400;white-space:nowrap}
  .fax .brand{position:absolute;left:28px;top:36px;font-size:13px}
  .fax .brand__mark{width:13px;height:13px}
  .fax__fields{position:absolute;left:28px;right:28px;top:90px;font-size:8px;color:var(--ink)}
  .fax__row{display:flex;border-bottom:1px solid var(--rule);padding:6px 0}
  .fax__row span{width:70px;font-weight:600}
  .fax .body-copy{position:absolute;left:28px;right:28px;top:230px}
  .fax .band{height:26px;padding-left:28px;font-size:8px}

  /* business card front */
  .card-front{left:776px;top:36px;width:384px;height:220px;border-radius:8px}
  .card-front .brand{position:absolute;left:26px;top:40px;font-size:15px}
  .card-front .brand__mark{width:15px;height:15px}
  .card-front__name{position:absolute;right:26px;top:72px;text-align:right;font-size:11px;font-weight:700;color:var(--red);white-space:nowrap}
  .card-front__name small{display:block;font-size:7px;color:var(--ink-soft);font-weight:400}
  .card-front .contact{position:absolute;left:26px;top:112px;font-size:7px}
  .card-front .band{height:28px;padding-left:26px;font-size:8.5px}

  /* business card back */
  .card-back{left:776px;top:276px;width:384px;height:220px;border-radius:8px;background:radial-gradient(circle at 30% 40%,var(--red-light),var(--red) 45%,var(--red-deep))}
  .card-back .brand{position:absolute;left:50%;top:50%;transform:translate(-50%,-60%);color:#fff;font-size:20px}
  .card-back .brand__mark{width:20px;height:20px;background:#fff}
  .card-back__web{position:absolute;right:24px;bottom:18px;color:#fff;font-size:9px;font-weight:600}

  /* envelope */
  .envelope{left:40px;top:540px;width:520px;height:284px}
  .envelope__flap{position:absolute;left:0;top:0;width:100%;height:130px}
  .envelope .brand{position:absolute;left:30px;top:150px;font-size:15px}
  .envelope .brand__mark{width:15px;height:15px}
  .envelope .contact{position:absolute;left:30px;top:178px}
  .envelope .band{height:26px;padding-left:30px;font-size:8px}

  /* compliment slip */
  .slip{left:580px;top:520px;width:580px;height:304px}
  .slip .brand{position:absolute;left:30px;top:30px;font-size:16px}
  .slip .brand__mark{width:16px;height:16px}
  .slip .contact{position:absolute;right:30px;top:28px;text-align:right}
  .slip__title{position:absolute;left:30px;top:90px;font-size:14px;color:var(--red);font-weight:400}
  .slip .body-copy{position:absolute;left:30px;right:30px;top:120px}
  .slip__web{position:absolute;left:30px;bottom:40px;font-size:9px;font-weight:600;color:var(--ink)}
  .slip .band{height:26px;padding-left:30px;font-size:8px}
</style>
</head>
<body>

<section class="sheet letterhead">
  <div class="brand"><span class="brand__mark"></span>Veromb Technologies</div>
  <address class="contact">
    Suite 24613 Lower Ground Floor<br>212-224 Harwell Road<br>London, N7 2QD<br>
    T: +44 (0)20 7946 0381<br>F: +44 (0)20 7946 0382<br>www.veromb.co.uk
  </address>
  <p class="greeting">Hello,</p>
  <p class="body-copy">Lorem Ipsum is simply dummy text of the printing and typesetting industry. Lorem Ipsum has been the industry's standard dummy text ever since the 1500s, when an unknown printer took a galley of type and scrambled it to make a type specimen book. It has survived not only five centuries, but also the leap into electronic typesetting, remaining essentially unchanged. It was popularised in the 1960s with the release of Letraset sheets containing Lorem Ipsum passages, and more recently with desktop publishing software like Aldus PageMaker including versions of Lorem Ipsum.<br><br>Lorem Ipsum is simply dummy text of the printing and typesetting industry. Lorem Ipsum has been the industry's standard dummy text ever since the 1500s, when an unknown printer took a galley of type and scrambled it to make a type specimen book.</p>
  <div class="band">Your Creative Line Goes Here. Your Creative Line Goes Here.</div>
</section>

<section class="sheet fax">
  <div class="brand"><span class="brand__mark"></span>Veromb Technologies</div>
  <h2 class="fax__title">Fax Sheet</h2>
  <div class="fax__fields">
    <div class="fax__row"><span>To:</span></div>
    <div class="fax__row"><span>From:</span></div>
    <div class="fax__row"><span>Fax:</span></div>
    <div class="fax__row"><span>Date:</span></div>
    <div class="fax__row"><span>Pages:</span></div>
  </div>
  <p class="body-copy">Lorem Ipsum is simply dummy text of the printing and typesetting industry. Lorem Ipsum has been the industry's standard dummy text ever since the 1500s, when an unknown printer took a galley of type and scrambled it to make a type specimen book. It has survived not only five centuries, but also the leap into electronic typesetting, remaining essentially unchanged.</p>
  <div class="band">Your Creative Line Goes Here. Your Creative Line Goes Here.</div>
</section>

<section class="sheet card-front">
  <div class="brand"><span class="brand__mark"></span>Veromb Technologies</div>
  <p class="card-front__name">Malcolm Dewhurst<small>CEO</small></p>
  <address class="contact">
    Suite 24613 Lower Ground Floor, 212-224 Harwell Road, London, N7 2QD<br>
    <strong>T:</strong> +44 (0)20 7946 0381 &nbsp; <strong>M:</strong> +44 (0)7700 900417<br>
    <strong>E:</strong> mdewhurst@veromb.co.uk<br>
    <strong>W:</strong> www.veromb.co.uk
  </address>
  <div class="band">Your Creative Line Goes Here. Your Creative Line Goes Here.</div>
</section>

<section class="sheet card-back">
  <div class="brand"><span class="brand__mark"></span>Veromb Technologies</div>
  <p class="card-back__web">www.veromb.co.uk</p>
</section>

<section class="sheet envelope">
  <svg class="envelope__flap" viewBox="0 0 520 130" preserveAspectRatio="none" aria-hidden="true">
    <polyline points="0,0 260,120 520,0" fill="none" stroke="#d9d9d9" stroke-width="1.5"/>
  </svg>
  <div class="brand"><span class="brand__mark"></span>Veromb Technologies</div>
  <address class="contact">Suite 24613 Lower Ground Floor<br>212-224 Harwell Road<br>London, N7 2QD</address>
  <div class="band">Your Creative Line Goes Here. Your Creative Line Goes Here.</div>
</section>

<section class="sheet slip">
  <div class="brand"><span class="brand__mark"></span>Veromb Technologies</div>
  <address class="contact">
    Suite 24613 Lower Ground Floor<br>212-224 Harwell Road, London, N7 2QD<br>
    T: +44 (0)20 7946 0381<br>mdewhurst@veromb.co.uk
  </address>
  <p class="slip__title">With Compliments</p>
  <p class="body-copy">Lorem Ipsum is simply dummy text of the printing and typesetting industry. Lorem Ipsum has been the industry's standard dummy text ever since the 1500s, when an unknown printer took a galley of type and scrambled it to make a type specimen book.</p>
  <p class="slip__web">www.veromb.co.uk</p>
  <div class="band">Your Creative Line Goes Here. Your Creative Line Goes Here.</div>
</section>

</body>
</html>
```